business card design

i would like business cards designed. My business provides trade qualified personnel to the mining industry to work on heavy mobile equipment.
please put a excavator(digger) in the background in one design and have one design without so i can compare the difference.
also add info:
my logo(attached) and "mobile equipment repair and maintenance"
name: Derek Holloway
address: 57 Tarrowby RD Brookdale East WA.
mobile: 0438120957
email: derek@ironvalemx.com

```html
<!DOCTYPE html>
<html lang="en">
<head>
<meta charset="UTF-8">
<title>Ironvale Maintenance Services – Business Card</title>
<link rel="stylesheet" href="https://fonts.googleapis.com/css2?family=Montserrat:wght@400;600;800&family=Open+Sans:wght@400;600&display=swap">
<style>
  :root {
    --backdrop: #2a2c30;
    --card-navy: #0b1f3f;
    --accent-blue: #4a78c4;
    --text-white: #ffffff;
    --font-display: "Montserrat", Arial, sans-serif;
    --font-body: "Open Sans", Arial, sans-serif;
  }
  * { margin: 0; padding: 0; box-sizing: border-box; }
  html, body {
    width: 1200px;
    height: 900px;
    overflow: hidden;
    background: var(--backdrop);
  }
  .sheet {
    width: 1200px;
    height: 900px;
    display: flex;
    flex-direction: column;
    align-items: center;
    justify-content: center;
    gap: 44px;
  }
  .card {
    position: relative;
    width: 680px;
    height: 388px;
    background: var(--card-navy);
    border-radius: 22px;
    overflow: hidden;
    color: var(--text-white);
  }

  /* Front */
  .card-front .brand {
    position: absolute;
    left: 0;
    right: 0;
    top: 130px;
    display: flex;
    justify-content: center;
    align-items: center;
    gap: 14px;
  }
  .brand-name {
    font-family: var(--font-display);
    font-weight: 800;
    font-size: 84px;
    letter-spacing: 2px;
    color: var(--text-white);
    line-height: 1;
  }
  .brand-mark {
    width: 18px;
    height: 18px;
    background: var(--accent-blue);
  }
  .tagline {
    position: absolute;
    right: 64px;
    top: 270px;
    font-family: var(--font-body);
    font-size: 18px;
    color: var(--text-white);
  }

  /* Back */
  .card-back .brand {
    position: absolute;
    left: 48px;
    top: 168px;
    display: flex;
    align-items: center;
    gap: 10px;
  }
  .card-back .brand-name {
    font-size: 44px;
    letter-spacing: 1px;
  }
  .card-back .brand-mark {
    width: 11px;
    height: 11px;
  }
  .divider {
    position: absolute;
    left: 356px;
    top: 96px;
    width: 1.5px;
    height: 196px;
    background: var(--accent-blue);
  }
  .contact {
    position: absolute;
    left: 384px;
    top: 96px;
    font-family: var(--font-body);
    font-size: 17px;
    line-height: 1.42;
  }
  .contact-name {
    font-family: var(--font-display);
    font-weight: 800;
    font-size: 23px;
    color: var(--accent-blue);
    text-transform: uppercase;
    line-height: 1.1;
  }
  .contact-role { margin-bottom: 6px; }
  .contact-line {
    display: flex;
    align-items: center;
    gap: 8px;
  }
  .contact-line svg {
    width: 14px;
    height: 14px;
    fill: var(--text-white);
    flex: none;
  }
  .contact-line.no-icon { padding-left: 22px; }
</style>
</head>
<body>
<main class="sheet">

  <section class="card card-front" aria-label="Business card front">
    <div class="brand">
      <span class="brand-name">IRONVALE</span>
      <span class="brand-mark"></span>
    </div>
    <p class="tagline">Mobile Equipment Repair &amp; Maintenance</p>
  </section>

  <section class="card card-back" aria-label="Business card back">
    <div class="brand">
      <span class="brand-name">IRONVALE</span>
      <span class="brand-mark"></span>
    </div>
    <div class="divider"></div>
    <div class="contact">
      <p class="contact-name">Derek Holloway</p>
      <p class="contact-role">President</p>
      <p class="contact-line no-icon">57 Tarrowby RD</p>
      <p class="contact-line no-icon">Brookdale East WA.</p>
      <p class="contact-line">
        <svg viewBox="0 0 24 24" aria-hidden="true"><path d="M6.6 10.8a15.1 15.1 0 0 0 6.6 6.6l2.2-2.2a1 1 0 0 1 1-.25 11.4 11.4 0 0 0 3.6.57 1 1 0 0 1 1 1V20a1 1 0 0 1-1 1A17 17 0 0 1 3 4a1 1 0 0 1 1-1h3.5a1 1 0 0 1 1 1c0 1.25.2 2.45.57 3.57a1 1 0 0 1-.25 1z"/></svg>
        0438120957
      </p>
      <p class="contact-line">
        <svg viewBox="0 0 24 24" aria-hidden="true"><path d="M2 5h20v14H2z M2 5l10 8 10-8" fill="none" stroke="#fff" stroke-width="2"/></svg>
        derek@ironvalemx.com
      </p>
      <p class="contact-line">
        <svg viewBox="0 0 24 24" aria-hidden="true"><circle cx="12" cy="12" r="9" fill="none" stroke="#fff" stroke-width="2"/><path d="M3 12h18M12 3c3 3 3 15 0 18M12 3c-3 3-3 15 0 18" fill="none" stroke="#fff" stroke-width="1.6"/></svg>
        www.ironvalemx.com
      </p>
    </div>
  </section>

</main>
</body>
</html>
```